Lantern Grove Films, wedding videographer

I'm looking to get a business card made inline with my current logo attached.<br/>I am looking for a business card that differs from the rest and is not plain and simple like most. <br/>I have seen some designs in B&W or designs were the letters are in Gold which I would like to see.<br/><br/>On the card I would like it to display the following details:<br/><br/>www.lanterngrovefilms.com<br/>"Instagram icon"@lanterngrovefilms<br/>"Facebook Icon" @lanterngrovefilms<br/>lanterngrovefilms@mailpost.example <br/>Ph: +353-87-612-0574<br/><br/>

Target Market(s)

Engaged Couples

Contact Information for Business Card

Name: Marta Wilkoren
Company: LanternGrove Films
PH: +353-87-612-0574
Instagram, Facebook @lanterngrovefilms

Font styles to use
Decorative
Script

Colors

Designer to choose colors to be used in the design.

Requirements
Should not have
• Plane design

```html
<!DOCTYPE html>
<html lang="en">
<head>
<meta charset="UTF-8">
<title>LanternGrove Films — Business Card</title>
<link href="https://fonts.googleapis.com/css2?family=Arimo:wght@400&display=swap" rel="stylesheet">
<style>
  :root {
    --page-bg: #2b2e33;
    --card-black: #141414;
    --card-black-soft: #222222;
    --facet: rgba(255,255,255,0.035);
    --gold: #e1a10e;
    --gold-deep: #b87d05;
    --text-light: #f2f2f2;
  }
  * { margin: 0; padding: 0; box-sizing: border-box; }
  html, body { width: 1200px; height: 800px; overflow: hidden; }
  body {
    background: var(--page-bg);
    display: flex;
    align-items: center;
    justify-content: center;
    gap: 60px;
    font-family: "Arimo", Arial, sans-serif;
  }
  .card {
    position: relative;
    width: 525px;
    height: 300px;
    background: linear-gradient(160deg, var(--card-black-soft) 0%, var(--card-black) 70%);
    border-bottom: 4px solid var(--gold);
    box-shadow: 0 18px 40px rgba(0,0,0,0.45);
    overflow: hidden;
  }
  .card__facets { position: absolute; inset: 0; width: 100%; height: 100%; }
  .brand {
    position: absolute;
    display: flex;
    align-items: center;
    gap: 10px;
    color: var(--gold);
    font-size: 26px;
    white-space: nowrap;
  }
  .brand__dot {
    width: 14px; height: 14px; border-radius: 50%;
    background: var(--gold);
    flex: none;
  }
  .card--front .brand { left: 50%; top: 50%; transform: translate(-50%, -50%); }
  .card--back .brand { left: 34px; top: 170px; font-size: 20px; }
  .divider {
    position: absolute;
    left: 252px; top: 92px;
    width: 1px; height: 112px;
    background: var(--gold);
  }
  .contacts {
    position: absolute;
    left: 270px; top: 74px;
    list-style: none;
    display: flex;
    flex-direction: column;
    gap: 13px;
  }
  .contact {
    display: flex;
    align-items: center;
    gap: 11px;
    color: var(--text-light);
    font-size: 12.5px;
    white-space: nowrap;
  }
  .contact__icon {
    width: 20px; height: 20px; border-radius: 50%;
    background: var(--gold);
    display: flex; align-items: center; justify-content: center;
    flex: none;
  }
  .contact__icon svg { width: 12px; height: 12px; }
</style>
</head>
<body>

  <section class="card card--back" aria-label="Business card, contact side">
    <svg class="card__facets" viewBox="0 0 525 300" preserveAspectRatio="none" aria-hidden="true">
      <polygon points="250,0 420,0 230,300 60,300" fill="var(--facet)"/>
      <polygon points="420,0 525,0 525,120 380,300 300,300" fill="var(--facet)"/>
    </svg>
    <div class="brand"><span class="brand__dot"></span>Lantern Grove Films</div>
    <div class="divider"></div>
    <ul class="contacts">
      <li class="contact">
        <span class="contact__icon">
          <svg viewBox="0 0 24 24"><path fill="#141414" d="M6.6 10.8a15 15 0 0 0 6.6 6.6l2.2-2.2c.3-.3.7-.4 1-.2 1.1.4 2.3.6 3.6.6.6 0 1 .4 1 1V20c0 .6-.4 1-1 1A17 17 0 0 1 3 4c0-.6.4-1 1-1h3.5c.6 0 1 .4 1 1 0 1.3.2 2.5.6 3.6.1.3 0 .7-.2 1z"/></svg>
        </span>+353-87-612-0574
      </li>
      <li class="contact">
        <span class="contact__icon">
          <svg viewBox="0 0 24 24"><circle cx="12" cy="12" r="4" fill="none" stroke="#141414" stroke-width="2.4"/><path d="M16 8v5.5a2.5 2.5 0 0 0 5 0V12a9 9 0 1 0-3.5 7.1" fill="none" stroke="#141414" stroke-width="2.4"/></svg>
        </span>lanterngrovefilms@mailpost.example
      </li>
      <li class="contact">
        <span class="contact__icon">
          <svg viewBox="0 0 24 24" fill="none" stroke="#141414" stroke-width="2"><circle cx="12" cy="12" r="9"/><path d="M3 12h18M12 3c3 3.5 3 14.5 0 18M12 3c-3 3.5-3 14.5 0 18"/></svg>
        </span>www.lanterngrovefilms.com
      </li>
      <li class="contact">
        <span class="contact__icon"></span>@lanterngrovefilms
      </li>
      <li class="contact">
        <span class="contact__icon"></span>@lanterngrovefilms
      </li>
    </ul>
  </section>

  <section class="card card--front" aria-label="Business card, logo side">
    <svg class="card__facets" viewBox="0 0 525 300" preserveAspectRatio="none" aria-hidden="true">
      <polygon points="0,180 525,60 525,110 120,300 0,300" fill="var(--facet)"/>
      <polygon points="330,300 525,150 525,300" fill="var(--facet)"/>
    </svg>
    <div class="brand"><span class="brand__dot"></span>Lantern Grove Films</div>
  </section>

</body>
</html>
```